Tess Marlowe Communication business card

I am starting a small, country-based business that offers writing, communication and marketing services to a wide range of clients, inner city big business, to mining, through to agriculture.

The appeal of my business is that it's mobile and flexible. It's just me, with lots of hands-on experience on construction and infrastructure projects.

I can provide the following services:

• Communication planning and management
• Issues and media management
• Marketing and communication materials
• Project management and strategy
• Government liaison
• Incident management communication
• Stakeholder management

It would be great to be able to use the elements of the business card design on other stationery.

Industry/Entity Type

Communication

Requirements
Must have
• The following information:

Tess Marlowe
M: 0427 391 864
E: tess@tmcommsmail.com

PO Box 152
Durrandale Q 4472
Nice to have
• a rural element (windmill, workboots, wheat stalk)

```html
<!DOCTYPE html>
<html lang="en">
<head>
<meta charset="utf-8">
<title>Tess Marlowe Communication – Business Card</title>
<link rel="stylesheet" href="https://fonts.googleapis.com/css2?family=Saira+Semi+Condensed:wght@400;500;600&display=swap">
<style>
  :root {
    --page-bg: #e9e7e1;
    --slate: #3a4a5c;
    --slate-light: #4a6078;
    --sky: #0093dd;
    --label-blue: #3a5a7c;
    --divider-blue: #4ab4ee;
    --white: #ffffff;
    --card-shadow: rgba(0, 0, 0, 0.18);
  }
  * { margin: 0; padding: 0; box-sizing: border-box; }
  html, body {
    width: 1200px;
    height: 900px;
    overflow: hidden;
    background: var(--page-bg);
    font-family: "Saira Semi Condensed", "Arial Narrow", sans-serif;
    font-stretch: semi-condensed;
  }
  .canvas { position: relative; width: 1200px; height: 900px; }

  .card { position: absolute; box-shadow: 0 10px 24px var(--card-shadow); overflow: hidden; }

  /* Front */
  .card-front {
    left: 73px; top: 57px; width: 654px; height: 423px;
    background: var(--slate);
  }
  .rural-artwork {
    position: absolute; left: 280px; top: 0; width: 374px; height: 423px;
  }
  .wordmark {
    position: absolute; left: 54px; top: 194px;
    color: var(--white);
    font-weight: 600;
    line-height: 1;
    text-transform: lowercase;
    white-space: nowrap;
  }
  .wordmark-name { display: block; font-size: 60px; letter-spacing: 2px; }
  .wordmark-sub { display: block; font-size: 22px; letter-spacing: 1px; text-align: right; margin-top: -2px; }

  /* Back */
  .card-back {
    left: 556px; top: 467px; width: 601px; height: 388px;
    background: var(--sky);
    color: var(--white);
  }
  .contact {
    position: absolute; left: 58px; top: 45px;
    font-size: 23px; font-weight: 500; line-height: 30px; letter-spacing: 0.5px;
    white-space: nowrap;
  }
  .contact .label { color: var(--label-blue); }
  .contact .address { margin-top: 30px; }

  .services {
    position: absolute; left: 24px; top: 249px; width: 553px; height: 120px;
  }
  .services-panel { position: absolute; inset: 0; }
  .services-list {
    position: absolute; right: 13px; top: 8px;
    list-style: none; text-align: right;
    font-size: 18px; font-weight: 500; line-height: 26.5px; letter-spacing: 0;
    white-space: nowrap;
  }
  .services-list .sep { color: var(--divider-blue); padding: 0 4px; }
</style>
</head>
<body>
<main class="canvas">

  <section class="card card-front" aria-label="Business card front">
    <svg class="rural-artwork" viewBox="0 0 374 423" role="img" aria-label="Silhouette of a country windmill with sails">
      <defs>
        <linearGradient id="artwork-tone" x1="0" y1="0" x2="1" y2="1">
          <stop offset="0" stop-color="#3a4a5c"/>
          <stop offset="1" stop-color="#4a6078"/>
        </linearGradient>
      </defs>
      <rect width="374" height="423" fill="url(#artwork-tone)"/>
    </svg>
    <div class="wordmark">
      <span class="wordmark-name">Tess Marlowe</span>
      <span class="wordmark-sub">Communication</span>
    </div>
  </section>

  <section class="card card-back" aria-label="Business card back">
    <div class="contact">
      <p>Tess Marlowe</p>
      <p><span class="label">M:</span> 0427 391 864</p>
      <p><span class="label">E:</span> tess@tmcommsmail.com</p>
      <p class="address">PO Box 152<br>Durrandale Q 4472</p>
    </div>

    <div class="services">
      <svg class="services-panel" viewBox="0 0 553 120" preserveAspectRatio="none" aria-hidden="true">
        <polygon points="0,0 553,0 553,120 38,120 0,92" fill="var(--slate)"/>
      </svg>
      <ul class="services-list">
        <li>Issues and media management<span class="sep">|</span>Project management and strategy</li>
        <li>Government liaison<span class="sep">|</span>Incident management communication</li>
        <li>Communication planning and management</li>
        <li>Stakeholder management<span class="sep">|</span>Marketing and communication</li>
      </ul>
    </div>
  </section>

</main>
</body>
</html>
```